Safety poster

I need a safety poster. The poster will be a picture of myself. I am wearing a prosthetic arm. In the hook is a "Lock out tag" I promote safety in the workplace. I am a motivational safety speaker. I want to leave posters after I have talked with companies- but also use these posters as advertisement. So- besides the safety slogan, my information needs to be on there too. (Contact info so someone would know how to get me for a speaking engagement)
I have made a few on my own and they are very popular. I think they could be done much better by a professional.
Some slogans:
Lock out complacency
Choose safety
100% preventable
If you don't think it will happen to you...think again
etc....
These posters are usually hung in workplace environments- break rooms and sometimes safety manager offices.
I like my photo in black and white with the "Lock out tag" in red.
I would also like some in full color.
The size will be 11X17 or something like that- they don't need to be very big- but big enough to be seen.
Information at bottom right of poster would say:
Book a Safety Presentation
with Dara Voss
612-555-0487
www.daravossmail.net
Target Market(s)
Manufacturing, hourly workers, salaried workers, safety management
Industry/Entity Type
Safety
Look and feel
Each slider illustrates characteristics of the customer's brand and the style your logo design should communicate.

```html
<!DOCTYPE html>
<html lang="en">
<head>
<meta charset="utf-8">
<title>Safety Poster Series</title>
<link href="https://fonts.googleapis.com/css2?family=Libre+Franklin:wght@400;700;900&display=swap" rel="stylesheet">
<style>
  :root {
    --ink: #111111;
    --paper: #ffffff;
    --safety-red: #d42a2a;
    --stage: #e4e4e4;
    --tile: #ecebe8;
    --mono-light: #d6d6d6;
    --mono-dark: #2a2a2a;
    --skin-light: #c9a384;
    --skin-dark: #3a2a20;
    --tag-cream: #e9e3d6;
  }
  * { box-sizing: border-box; margin: 0; padding: 0; }
  html, body { width: 1200px; height: 600px; overflow: hidden; }
  body {
    background: var(--stage);
    font-family: "Libre Franklin", Arial, sans-serif;
    position: relative;
  }
  .poster {
    position: absolute;
    top: 146px;
    width: 200px;
    height: 308px;
    background: var(--paper);
    overflow: hidden;
  }
  .poster--one   { left: 26px; }
  .poster--two   { left: 263px; }
  .poster--three { left: 500px; }
  .poster--four  { left: 737px; }
  .poster--five  { left: 974px; }

  .band {
    position: absolute; left: 0; top: 0;
    width: 100%; height: 96px;
    background: var(--ink);
  }
  .headline {
    position: absolute;
    z-index: 2;
    font-weight: 900;
    line-height: 0.9;
    text-transform: uppercase;
    letter-spacing: -0.5px;
    white-space: nowrap;
  }
  .headline--stat { left: 8px; top: 8px; color: var(--paper); font-size: 62px; letter-spacing: -2px; }
  .headline--stat-sub { left: 9px; top: 66px; color: var(--paper); font-size: 22px; }
  .headline--question { left: 10px; top: 20px; color: var(--ink); font-size: 15.5px; line-height: 1.05; }
  .headline--question .accent { color: var(--safety-red); border-bottom: 3px solid var(--safety-red); }
  .headline--answer { left: 10px; top: 140px; color: var(--safety-red); font-size: 19px; line-height: 0.95; letter-spacing: -1px; }
  .headline--lockout { left: 8px; top: 38px; color: var(--paper); font-size: 31px; letter-spacing: -1px; }
  .headline--lockout-sub { left: 8px; top: 67px; color: var(--paper); font-size: 22px; letter-spacing: -1px; }
  .headline--choose { left: 9px; top: 30px; color: var(--ink); font-size: 29px; line-height: 0.88; }
  .headline--choose .accent { color: var(--safety-red); }

  .tile-field {
    position: absolute; inset: 0;
    background: linear-gradient(160deg, #f6f6f4 0%, var(--tile) 100%);
  }
  .edge-stripe {
    position: absolute; left: 0; top: 0;
    width: 6px; height: 100%;
    background: var(--safety-red);
  }
  .tagline {
    position: absolute; left: 10px; top: 84px;
    font-size: 5px; color: var(--ink);
  }
  .check-mark {
    position: absolute; left: 130px; top: 26px;
    width: 56px; height: 56px;
  }
  .prohibit-sign {
    position: absolute; left: 0; top: 0;
    width: 130px; height: 96px;
  }
  .lock-tag {
    position: absolute; left: 150px; top: 0;
    width: 50px; height: 110px;
    background: linear-gradient(180deg, var(--tag-cream) 0%, var(--tag-cream) 70%, var(--safety-red) 70%);
    border-radius: 0 0 4px 4px;
  }

  .photo {
    position: absolute;
    left: 82px; top: 104px;
    width: 116px; height: 204px;
    border-radius: 36px 36px 0 0;
  }
  .photo--mono {
    background: linear-gradient(180deg, var(--mono-light) 0%, #9a9a9a 45%, var(--mono-dark) 100%);
  }
  .photo--colour {
    background: linear-gradient(180deg, var(--skin-light) 0%, #8b6547 45%, var(--skin-dark) 100%);
  }
  .poster--two .photo { top: 122px; height: 186px; }

  .marker-bar {
    position: absolute; left: 0; top: 250px;
    width: 6px; height: 22px;
    background: var(--ink);
  }
  .contact {
    position: absolute; left: 10px; top: 248px;
    z-index: 2;
    color: var(--ink);
    white-space: nowrap;
  }
  .contact__name { font-size: 9px; font-weight: 700; line-height: 1.1; }
  .contact__role { font-size: 4.5px; line-height: 1.3; }
  .contact__phone { font-size: 7px; font-weight: 700; line-height: 1.2; }
  .contact__web { font-size: 5px; font-weight: 700; line-height: 1.2; }
  .contact--placeholder { top: 252px; }
  .contact--placeholder p { font-size: 4px; line-height: 1.5; }
  .cursor {
    position: absolute; left: 50px; top: 284px;
    width: 9px; height: 13px;
    z-index: 2;
  }
</style>
</head>
<body>

  <section class="poster poster--one">
    <div class="band"></div>
    <h2 class="headline headline--stat">100%</h2>
    <h2 class="headline headline--stat-sub">Preventable</h2>
    <div class="photo photo--mono" role="img" aria-label="Black and white portrait of the speaker seated, holding a red lock out tag in her prosthetic hook"></div>
    <div class="contact">
      <p class="contact__name">Dara Voss</p>
      <p class="contact__role">motivational safety speaker</p>
      <p class="contact__phone">612-555-0487</p>
      <p class="contact__web">www.daravossmail.net</p>
    </div>
    <svg class="cursor" viewBox="0 0 9 13"><path d="M0 0 L0 11 L3 8.5 L5 12.5 L6.5 12 L4.5 8 L8.5 8 Z" fill="#111"/></svg>
  </section>

  <section class="poster poster--two">
    <h2 class="headline headline--question">If you don't<br>think it will<br>happen to <span class="accent">you</span></h2>
    <div class="lock-tag" role="img" aria-label="Do not operate lock out tag with red padlock"></div>
    <h2 class="headline headline--answer">Think<br>again!</h2>
    <div class="photo photo--mono" role="img" aria-label="Black and white portrait of the speaker seated, holding a red lock out tag in her prosthetic hook"></div>
    <div class="marker-bar"></div>
    <div class="contact">
      <p class="contact__name">Dara Voss</p>
      <p class="contact__role">motivational safety speaker</p>
      <p class="contact__phone">612-555-0487</p>
      <p class="contact__web">www.daravossmail.net</p>
    </div>
  </section>

  <section class="poster poster--three">
    <div class="band"></div>
    <svg class="prohibit-sign" viewBox="0 0 130 96">
      <circle cx="62" cy="36" r="46" fill="none" stroke="#d42a2a" stroke-width="11"/>
      <line x1="30" y1="4" x2="94" y2="68" stroke="#d42a2a" stroke-width="11"/>
    </svg>
    <h2 class="headline headline--lockout">Lock out</h2>
    <h2 class="headline headline--lockout-sub">Complacency</h2>
    <div class="photo photo--mono" role="img" aria-label="Black and white portrait of the speaker seated, holding a red lock out tag in her prosthetic hook"></div>
    <div class="contact">
      <p class="contact__name">Dara Voss</p>
      <p class="contact__role">motivational safety speaker</p>
      <p class="contact__phone">612-555-0487</p>
      <p class="contact__web">www.daravossmail.net</p>
    </div>
    <svg class="cursor" viewBox="0 0 9 13"><path d="M0 0 L0 11 L3 8.5 L5 12.5 L6.5 12 L4.5 8 L8.5 8 Z" fill="#111"/></svg>
  </section>

  <section class="poster poster--four">
    <div class="tile-field"></div>
    <div class="edge-stripe"></div>
    <h2 class="headline headline--choose">Choose<br><span class="accent">Safety</span></h2>
    <svg class="check-mark" viewBox="0 0 56 56">
      <circle cx="26" cy="30" r="22" fill="none" stroke="#d42a2a" stroke-width="3"/>
      <path d="M12 30 L23 42 L50 8" fill="none" stroke="#d42a2a" stroke-width="7" stroke-linejoin="miter"/>
    </svg>
    <p class="tagline">motivational safety speaker</p>
    <div class="photo photo--mono" role="img" aria-label="Black and white portrait of the speaker seated, holding a red lock out tag in her prosthetic hook"></div>
    <div class="marker-bar"></div>
    <div class="contact contact--placeholder">
      <p>Contact me for a speaking engagement</p>
      <p>Name Here</p>
      <p>000 000 0000</p>
    </div>
  </section>

  <section class="poster poster--five">
    <div class="tile-field"></div>
    <div class="edge-stripe"></div>
    <h2 class="headline headline--choose">Choose<br><span class="accent">Safety</span></h2>
    <svg class="check-mark" viewBox="0 0 56 56">
      <circle cx="26" cy="30" r="22" fill="none" stroke="#d42a2a" stroke-width="3"/>
      <path d="M12 30 L23 42 L50 8" fill="none" stroke="#d42a2a" stroke-width="7" stroke-linejoin="miter"/>
    </svg>
    <div class="photo photo--colour" role="img" aria-label="Full colour portrait of the speaker seated, holding a red lock out tag in her prosthetic hook"></div>
    <div class="marker-bar"></div>
    <div class="contact">
      <p class="contact__name">Dara Voss</p>
      <p class="contact__role">motivational safety speaker</p>
      <p class="contact__phone">612-555-0487</p>
      <p class="contact__web">www.daravossmail.net</p>
    </div>
  </section>

</body>
</html>
```